New to ArtHarbor? This Contest is for you!

Are you new to ArtHarbor and looking to enter your first contest? Look no further! We're launching this special contest to help you get started on building a design portfolio at ArtHarbor!

Requirements:
* Create a beautiful and eye-catching graphic design which includes the words "Spot me at ArtHarbor!"
* Upload your design to this contest AND share it on Chatterly
* You must upload your entry before 12:00am 1 April
* This must be your very FIRST entry on ArtHarbor to be eligible to receive a prize. If you've already entered other ArtHarbor contests you won't be eligible to win the prizes
* Your design must adhere to our quality standards to be eligible to receive a prize

Prizes:
* There are 150 x $5 participation payments ($750) available to be awarded to high-quality designs
* First prize for the best design is $150
* Second prize is $100

Requirements
Must have
• Your design must contain the words "Spot me at ArtHarbor".
• This must be your first entry on ArtHarbor to be eligible for the prizes.
• Your design must adhere to our quality standards.
Should not have
• No stock images or overused concepts.

```html
<!DOCTYPE html>
<html lang="en">
<head>
<meta charset="utf-8">
<title>Spot me at ArtHarbor</title>
<link rel="stylesheet" href="https://fonts.googleapis.com/css2?family=Fredoka:wght@600;700&family=Quicksand:wght@300&display=swap">
<style>
  :root {
    --paper: #ffffff;
    --sky-deep: #0a9fe0;
    --sky-mid: #45c2f0;
    --sky-soft: #7fd3f5;
    --frame-line: #4ab8ea;
    --coin-edge: #0b7fb5;
  }
  html, body {
    margin: 0;
    padding: 0;
    width: 1200px;
    height: 1000px;
    overflow: hidden;
    background: var(--paper);
  }
  .canvas {
    position: relative;
    width: 1200px;
    height: 1000px;
  }
  .artwork {
    position: absolute;
    inset: 0;
  }
  .brand-name {
    position: absolute;
    left: 62px;
    top: 186px;
    display: flex;
    align-items: center;
    gap: 24px;
    margin: 0;
    font-family: "Fredoka", sans-serif;
    font-size: 54px;
    font-weight: 600;
    letter-spacing: 2px;
    color: var(--sky-deep);
    line-height: 1;
    white-space: nowrap;
  }
  .brand-dot {
    width: 44px;
    height: 44px;
    border-radius: 50%;
    background: var(--sky-deep);
  }
  .tagline {
    position: absolute;
    left: 480px;
    top: 756px;
    width: 690px;
    margin: 0;
    font-size: 56px;
    line-height: 1;
    letter-spacing: 1px;
    white-space: nowrap;
  }
  .tagline .strong {
    font-family: "Fredoka", sans-serif;
    font-weight: 700;
    color: var(--sky-deep);
  }
  .tagline .soft {
    font-family: "Fredoka", sans-serif;
    font-weight: 700;
    color: var(--sky-soft);
  }
  .tagline .thin {
    font-family: "Quicksand", sans-serif;
    font-weight: 300;
    color: var(--sky-mid);
    letter-spacing: 2px;
  }
  .coin-name {
    font-family: "Fredoka", sans-serif;
    font-weight: 600;
    font-size: 44px;
    letter-spacing: 2px;
    fill: var(--coin-edge);
  }
</style>
</head>
<body>
<main class="canvas">
  <svg class="artwork" width="1200" height="1000" viewBox="0 0 1200 1000">
    <defs>
      <linearGradient id="sea" x1="0" y1="0" x2="0.3" y2="1">
        <stop offset="0" stop-color="#ffffff"/>
        <stop offset="0.35" stop-color="#c8ecfb"/>
        <stop offset="0.7" stop-color="#6fcdf3"/>
        <stop offset="1" stop-color="#2bb6ec"/>
      </linearGradient>
      <radialGradient id="glow" cx="0.5" cy="0.5" r="0.5">
        <stop offset="0" stop-color="#ffffff" stop-opacity="0.95"/>
        <stop offset="1" stop-color="#ffffff" stop-opacity="0"/>
      </radialGradient>
      <linearGradient id="disc" x1="0" y1="0" x2="1" y2="1">
        <stop offset="0" stop-color="#bfe9fb"/>
        <stop offset="0.5" stop-color="#ffffff"/>
        <stop offset="1" stop-color="#29aee6"/>
      </linearGradient>
      <linearGradient id="coin-face" x1="0" y1="0" x2="0" y2="1">
        <stop offset="0" stop-color="#4fbbea"/>
        <stop offset="1" stop-color="#eaf8fe"/>
      </linearGradient>
      <linearGradient id="coin-rim" x1="0" y1="0" x2="1" y2="1">
        <stop offset="0" stop-color="#8fd8f6"/>
        <stop offset="1" stop-color="#0b7fb5"/>
      </linearGradient>
    </defs>

    <g role="img" aria-label="Shimmering blue water surface with a light lattice pattern and sparkles">
      <rect class="art-field" x="15" y="262" width="1172" height="565" fill="url(#sea)"/>
      <circle cx="1110" cy="310" r="90" fill="url(#glow)"/>
      <circle cx="390" cy="745" r="70" fill="url(#glow)"/>
      <circle cx="40" cy="600" r="80" fill="url(#glow)"/>
    </g>

    <g class="disc disc-top">
      <ellipse cx="230" cy="378" rx="175" ry="90" fill="#1592cc"/>
      <ellipse cx="230" cy="368" rx="175" ry="90" fill="url(#disc)"/>
    </g>
    <g class="disc disc-bottom">
      <ellipse cx="975" cy="628" rx="185" ry="92" fill="#1592cc"/>
      <ellipse cx="975" cy="618" rx="185" ry="92" fill="url(#disc)"/>
    </g>

    <g class="medallion">
      <ellipse cx="612" cy="492" rx="206" ry="225" fill="url(#coin-rim)"/>
      <ellipse cx="598" cy="492" rx="205" ry="222" fill="#ffffff" opacity="0.55"/>
      <ellipse cx="600" cy="492" rx="196" ry="213" fill="none" stroke="var(--coin-edge)" stroke-width="10"/>
      <ellipse cx="594" cy="496" rx="176" ry="192" fill="url(#coin-face)" stroke="#0e86bd" stroke-width="4"/>
      <text class="coin-name" x="594" y="486" text-anchor="middle">OPENFIELD</text>
      <text class="coin-name" x="594" y="540" text-anchor="middle">IMAGES</text>
    </g>

    <g class="frame-top">
      <rect x="0" y="160" width="760" height="101" fill="var(--paper)"/>
      <path d="M0 262 H735 Q760 262 760 237 V168" fill="var(--paper)"/>
      <path d="M15 262 H735 Q760 262 760 237 V168" fill="none" stroke="var(--frame-line)" stroke-width="2"/>
    </g>

    <g class="frame-bottom">
      <path d="M442 827 V762 Q442 737 467 737 H1187 V827 Z" fill="var(--paper)"/>
      <path d="M442 827 V762 Q442 737 467 737 H1187" fill="none" stroke="var(--frame-line)" stroke-width="2"/>
    </g>
  </svg>

  <h1 class="brand-name">OPENFIELD IMAGES <span class="brand-dot"></span></h1>

  <p class="tagline"><span class="strong">SPOT</span> <span class="soft">ME AT</span> <span class="thin">ARTHARBOR</span></p>
</main>
</body>
</html>
```